Cell Tower company needs website updated

We need a website that does not look like it was designed in the early 1990's. The company fabricates, installs and reinforces communication towers throughout the US, Caribbean, Central and S. America. We are located in Pensacola Florida. Our tower technicians travel to wherever the work is. I have some good pictures taken from towers to use on the site. I want the site to reflect the excitement that the wireless communication industry has. I want to the company to look exciting and attract new employees. The majority of our business is modifying and reinforcing existing cell towers to accept all the new tower top antennas that the increasing wireless mobile world demands.
Updates

I have added some sample photos from our business to our ArtBazaar profile.

We are now going through each design to find what is most suitable for our needs. Thank you all for your time in this matter.

Industry/Entity Type

Wireless Communication

```html
<!DOCTYPE html>
<html lang="en">
<head>
<meta charset="utf-8">
<title>TowerCrest Incorporated</title>
<link href="https://fonts.googleapis.com/css2?family=PT+Sans:wght@400;700&family=Open+Sans:wght@400;600;700&display=swap" rel="stylesheet">
<style>
:root{
  --red:#c4000b;
  --ink:#333333;
  --muted:#7a7a7a;
  --line:#e2e2d6;
  --cream:#efece0;
  --band:#e9e5d3;
  --charcoal:#2b2b2b;
  --coal:#1f1f1f;
  --white:#ffffff;
  --footer-text:#a5a5a5;
  --footer-link:#cfcfcf;
}
*{box-sizing:border-box;margin:0;padding:0}
html,body{width:1200px;height:2652px;overflow:hidden;background:var(--white)}
body{font-family:"Open Sans",Arial,sans-serif;color:var(--ink);font-size:12px;line-height:1.5}
.page{position:relative;width:1200px;height:2652px;overflow:hidden}
.abs{position:absolute}
h2,h3,h4,h5{font-family:"PT Sans",Arial,sans-serif;font-weight:700;text-transform:uppercase}
h5{text-transform:none}
p{color:var(--muted)}

/* top bar */
.topbar{left:0;top:0;width:1200px;height:57px;background:var(--charcoal)}
.topbar-red{left:0;top:0;width:990px;height:57px;background:var(--red)}
.topbar-item{top:0;height:57px;display:flex;align-items:center;gap:9px;color:var(--white);font-size:14px;font-weight:600}
.topbar-item svg{flex:none}

/* header */
.brand{left:144px;top:88px;display:flex;align-items:center;gap:10px}
.brand-mark{width:18px;height:18px;background:var(--red);border-radius:50%}
.brand-name{font-family:"PT Sans",Arial,sans-serif;font-weight:700;font-size:40px;color:#2a2a2a;line-height:1}
.brand-sub{left:330px;top:134px;font-family:"PT Sans",Arial,sans-serif;font-weight:700;font-size:10px;letter-spacing:3px;color:#2a2a2a}
.nav{right:136px;top:128px;display:flex;gap:30px;font-family:"PT Sans",Arial,sans-serif;font-weight:700;font-size:15px;text-transform:uppercase;color:#333}
.nav .active{color:var(--red)}

/* hero */
.hero{left:0;top:190px;width:1200px;height:407px;background:linear-gradient(180deg,#8aa6c4 0%,#b4c2cf 38%,#8a7a5e 52%,#c49a3e 70%,#b0832c 100%)}
.hero-title{left:0;top:325px;width:1200px;text-align:center;color:var(--white);font-size:46px;line-height:56px}
.hero-btn{left:487px;top:472px;width:226px;height:34px;border:2px solid var(--white);color:var(--white);font-family:"PT Sans",Arial,sans-serif;font-weight:700;font-size:16px;display:flex;align-items:center;justify-content:center;text-transform:uppercase}
.hero-dots{left:555px;top:551px;display:flex;gap:9px}
.hero-dots span{width:8px;height:8px;border-radius:50%;background:rgba(255,255,255,.85)}

/* features */
.feature{top:655px;width:240px;text-align:center}
.feature-icon{margin:0 auto;width:86px;height:86px;border-radius:50%;background:var(--red);display:flex;align-items:center;justify-content:center}
.feature h3{margin-top:24px;font-size:20px;color:#333}
.btn-outline{display:inline-flex;align-items:center;justify-content:center;margin-top:16px;width:118px;height:34px;border:2px solid #d8d8d8;color:var(--red);font-family:"PT Sans",Arial,sans-serif;font-weight:700;font-size:13px;text-transform:uppercase}

.rule{left:181px;width:836px;height:2px;background:var(--line)}

/* who we are */
.section-label{font-family:"PT Sans",Arial,sans-serif;font-weight:700;font-size:14px;text-transform:uppercase;color:#333}
.who-photo{top:972px;width:190px;height:104px;border-radius:2px}
.who-copy{left:800px;top:964px;width:210px}
.who-copy h4{color:var(--red);font-size:13px;line-height:18px}
.who-copy p{font-size:10px;line-height:15px;margin-top:6px}
.more{display:flex;align-items:center;gap:10px;font-size:11px;color:#555}
.more i{width:18px;height:18px;border-radius:50%;background:var(--red);display:inline-flex;align-items:center;justify-content:center}

/* help banner */
.help{left:181px;top:1136px;width:626px;height:82px;background:var(--cream);padding:18px 38px}
.help h4{font-size:14px;color:#333}
.help h4 span{color:var(--red)}
.help p{font-size:10px;margin-top:8px}
.help-cta{left:807px;top:1136px;width:210px;height:82px;background:var(--red);color:var(--white);font-family:"PT Sans",Arial,sans-serif;font-weight:700;font-size:19px;display:flex;align-items:center;justify-content:center;text-transform:uppercase}

/* projects */
.projects-copy{left:181px;top:1268px;width:200px}
.projects-copy p{font-size:10px;line-height:15px;margin-top:6px}
.project{top:1273px;width:194px}
.project-img{width:194px;height:124px;background:linear-gradient(180deg,#3f8be0 0%,#6fa9ea 60%,#9cc3ee 100%)}
.project p{font-size:10px;line-height:15px;text-align:center;margin-top:14px}

/* services */
.service-title{left:0;top:1506px;width:1200px;text-align:center}
.service-title span{background:var(--white);padding:0 22px;font-family:"PT Sans",Arial,sans-serif;font-weight:700;font-size:15px;color:#444;text-transform:uppercase}
.service{width:205px;display:flex;gap:12px}
.service .num{flex:none;width:26px;height:26px;border-radius:50%;background:var(--red);color:var(--white);font-family:"PT Sans",Arial,sans-serif;font-weight:700;font-size:15px;display:flex;align-items:center;justify-content:center}
.service h4{font-size:13px;color:#333;line-height:16px}
.service p{font-size:10px;line-height:14px;margin-top:3px}

/* lower columns */
.col-head{font-family:"PT Sans",Arial,sans-serif;font-weight:700;font-size:14px;text-transform:uppercase;color:#333}
.event{left:181px;width:250px;display:flex;gap:14px}
.date{flex:none;width:40px;height:40px;background:var(--red);color:var(--white);text-align:center;font-family:"PT Sans",Arial,sans-serif;font-weight:700;font-size:15px;line-height:22px;padding-top:3px}
.date small{display:block;font-size:8px;line-height:8px;font-weight:400}
.date.past{background:#8f8f8f}
.event h5{font-size:12px;color:var(--red)}
.event h5.dark{color:#333}
.event .meta{font-size:8px;color:#999}
.event p{font-size:10px;line-height:14px;margin-top:10px}
.news{left:488px;width:260px;display:flex;gap:14px;align-items:flex-start;font-size:11px;color:#444}
.news .box{flex:none;width:18px;height:18px;background:#8f8f8f;color:var(--white);display:flex;align-items:center;justify-content:center;font-weight:700;font-size:14px;line-height:1}
.news .box.open{background:var(--red)}
.news.hot{color:var(--red)}
.quote{left:762px;top:1825px;width:255px;height:92px;background:var(--red);color:var(--white);padding:14px 28px 10px 46px;font-size:10px;line-height:14px}
.quote::after{content:"";position:absolute;left:206px;bottom:-14px;border-left:14px solid transparent;border-top:14px solid var(--red)}
.quote-mark{position:absolute;font-family:"PT Sans",Arial,sans-serif;font-weight:700;font-size:34px;line-height:1}

/* slogan band */
.band{left:0;top:2088px;width:1200px;height:248px;background:var(--band)}
.slogan-img{left:181px;top:2137px;width:400px;height:157px;background:linear-gradient(120deg,#4d6f93 0%,#7f98ae 45%,#d9d3c3 75%,#e7c04e 100%)}
.slogan-tag{left:181px;top:2220px;width:270px;height:52px;background:rgba(255,255,255,.78);color:var(--red);font-family:"PT Sans",Arial,sans-serif;font-weight:700;font-size:22px;display:flex;align-items:center;padding-left:28px;text-transform:uppercase}
.top-project{left:581px;top:2137px;width:436px;height:157px;background:var(--red);color:var(--white);padding:28px 44px}
.top-project h3{font-size:22px}
.top-project p{color:var(--white);font-size:10px;line-height:14px;margin-top:8px}
.top-project .more{color:var(--white);margin-top:20px}
.top-project .more i{background:var(--white)}

/* footer */
.footer{left:0;top:2336px;width:1200px;height:227px;background:var(--charcoal)}
.footer-col h4{font-size:15px;color:var(--white);line-height:20px}
.footer-col p{color:var(--footer-text);font-size:11px;line-height:15px;margin-top:12px}
.footer-link{color:var(--footer-link);font-size:11px;display:flex;align-items:center;gap:10px}
.thumb{width:80px;height:46px;background:linear-gradient(180deg,#3f7fcf,#9dbce0)}
.subscribe{left:844px;top:2468px;display:flex}
.subscribe .field{width:160px;height:26px;background:#eeeeee;font-size:10px;color:#999;display:flex;align-items:center;justify-content:center}
.subscribe .send{width:56px;height:26px;background:var(--red);color:var(--white);font-size:10px;display:flex;align-items:center;justify-content:center}
.bottombar{left:0;top:2563px;width:1200px;height:89px;background:var(--coal)}
.copyright{left:141px;top:2600px;color:var(--white);font-size:13px;font-weight:600}
.legal{left:362px;top:2600px;display:flex;gap:14px;color:var(--white);font-size:12px;font-weight:600}
.legal .sep{color:#777}
.social{left:874px;top:2597px;display:flex;gap:12px}
.social span{width:24px;height:24px;border-radius:50%;background:#555}
</style>
</head>
<body>
<div class="page">

  <!-- top bar -->
  <div class="abs topbar"></div>
  <div class="abs topbar-red"></div>
  <div class="abs topbar-item" style="left:141px">
    <svg width="16" height="16" viewBox="0 0 16 16"><circle cx="8" cy="8" r="8" fill="#fff"/><path d="M5 4.5l1.5-.5 1 2-1 1c.5 1 1.3 1.8 2.3 2.3l1-1 2 1-.5 1.5c-3.5 0-6.3-2.8-6.3-6.3z" fill="#c4000b"/></svg>
    +800 555 0142 or 916 555 0187
  </div>
  <div class="abs topbar-item" style="left:400px">
    <svg width="16" height="16" viewBox="0 0 16 16"><circle cx="8" cy="8" r="8" fill="#fff"/><rect x="4" y="5" width="8" height="6" fill="#c4000b"/><path d="M4 5l4 3 4-3" stroke="#fff" fill="none"/></svg>
    hello@towercrest.net
  </div>
  <div class="abs topbar-item" style="left:590px">
    <svg width="16" height="16" viewBox="0 0 16 16"><circle cx="8" cy="8" r="8" fill="#fff"/><path d="M4 5h8v5H8l-2 2v-2H4z" fill="#c4000b"/></svg>
    live chat
  </div>
  <div class="abs topbar-item" style="left:1038px">
    <svg width="16" height="16" viewBox="0 0 16 16"><circle cx="8" cy="8" r="8" fill="#fff"/><circle cx="7" cy="7" r="3" fill="none" stroke="#2b2b2b" stroke-width="1.6"/><path d="M9.2 9.2l2.6 2.6" stroke="#2b2b2b" stroke-width="1.6"/></svg>
  </div>

  <!-- header -->
  <div class="abs brand"><span class="brand-mark"></span><span class="brand-name">TowerCrest</span></div>
  <div class="abs brand-sub">INCORPORATED</div>
  <nav class="abs nav">
    <span class="active">Home</span><span>About us</span><span>Services</span><span>Blog</span><span>FAQs</span><span>Contact us</span>
  </nav>

  <!-- hero -->
  <div class="abs hero" role="img" aria-label="Photo of a cell tower with antennas on a golden plain below mountains and a blue sky"></div>
  <h2 class="abs hero-title">Voluptatem doloremque<br>ratione dolores</h2>
  <div class="abs hero-btn">Claim free consultation</div>
  <div class="abs hero-dots"><span></span><span></span><span></span><span></span><span></span></div>

  <!-- features -->
  <div class="abs feature" style="left:200px">
    <div class="feature-icon"><svg width="40" height="40" viewBox="0 0 40 40"><circle cx="20" cy="20" r="18" fill="#fff"/><path d="M10 27l7-9 5 6 3-3 5 6z" fill="#c4000b"/><circle cx="25" cy="14" r="3" fill="#c4000b"/></svg></div>
    <h3>Voluptatem</h3>
    <span class="btn-outline">Learn more</span>
  </div>
  <div class="abs feature" style="left:477px">
    <div class="feature-icon"><svg width="40" height="40" viewBox="0 0 40 40"><circle cx="20" cy="20" r="18" fill="#fff"/><rect x="10" y="13" width="20" height="14" rx="1" fill="#c4000b"/><path d="M10 13l10 8 10-8" stroke="#fff" stroke-width="2" fill="none"/></svg></div>
    <h3>Doloremque</h3>
    <span class="btn-outline">Learn more</span>
  </div>
  <div class="abs feature" style="left:757px">
    <div class="feature-icon"><svg width="40" height="40" viewBox="0 0 40 40"><circle cx="20" cy="20" r="18" fill="#fff"/><circle cx="20" cy="20" r="11" fill="#c4000b"/><path d="M13 15c3 0 4 2 6 2s1 4 3 5-1 5-3 5c0-3-3-3-3-6s-3-2-3-6zM24 12c2 1 5 4 5 8-2 0-3-2-4-3s-2-3-1-5z" fill="#fff"/></svg></div>
    <h3>Dolores unde</h3>
    <span class="btn-outline">Learn more</span>
  </div>

  <div class="abs rule" style="top:893px"></div>

  <!-- who we are -->
  <div class="abs section-label" style="left:181px;top:937px">Who we are</div>
  <div class="abs who-photo" style="left:181px;background:linear-gradient(135deg,#7d8b99,#c4c9cf 55%,#e4d23a)" role="img" aria-label="Video still of tower technicians in hard hats and safety vests"></div>
  <div class="abs" style="left:262px;top:1010px;width:28px;height:28px;border-radius:50%;background:rgba(255,255,255,.9)"></div>
  <svg class="abs" style="left:272px;top:1017px" width="12" height="14" viewBox="0 0 12 14"><path d="M0 0l12 7-12 7z" fill="#2b2b2b"/></svg>
  <div class="abs who-photo" style="left:385px;background:linear-gradient(135deg,#3b3f42,#8b8e85 55%,#c8a06a)" role="img" aria-label="Photo of technicians working inside an equipment shelter"></div>
  <div class="abs who-photo" style="left:588px;background:linear-gradient(135deg,#5a4a36,#b6874b 50%,#e3a93c)" role="img" aria-label="Photo of a technician in an orange hard hat at machinery"></div>
  <div class="abs who-copy">
    <h4>Welcome to<br>consequuntur</h4>
    <p>Voluptatem doloremque perspi beatae ratione dolores unde natus</p>
    <div class="more" style="margin-top:12px">learn more <i><svg width="8" height="8" viewBox="0 0 8 8"><path d="M2 1l4 3-4 3" stroke="#fff" stroke-width="1.6" fill="none"/></svg></i></div>
  </div>

  <!-- help banner -->
  <div class="abs help">
    <h4><span>Need help with your cell tower?</span> Sed enim accusantium laudantium inventore</h4>
    <p>Sed enim accusantium laudantium Unde quasi quae ratione inventore ipsa iste sunt sit ipsam ut voluptatem</p>
  </div>
  <div class="abs help-cta">Contact us now</div>

  <!-- recent projects -->
  <div class="abs projects-copy">
    <div class="section-label">Recent projects</div>
    <p>Dolores ut voluptatem doloremque perspi beatae quia ratione dolores unde Unde quasi ratione inventore ipsa explicabo</p>
    <div class="more" style="margin-top:14px">view more <i><svg width="8" height="8" viewBox="0 0 8 8"><path d="M2 1l4 3-4 3" stroke="#fff" stroke-width="1.6" fill="none"/></svg></i></div>
  </div>
  <div class="abs project" style="left:404px">
    <div class="project-img" role="img" aria-label="Photo of technicians climbing a lattice tower against a blue sky"></div>
    <p>Nemo rem ipsum quas illo<br>dolores ut voluptatem explicabo</p>
  </div>
  <div class="abs project" style="left:612px">
    <div class="project-img" role="img" aria-label="Photo of antenna arrays on a monopole against a blue sky"></div>
    <p>Nemo rem ipsum quas illo<br>dolores ut voluptatem explicabo</p>
  </div>
  <div class="abs project" style="left:820px">
    <div class="project-img" role="img" aria-label="Photo of a worker on a tower top antenna platform"></div>
    <p>Nemo rem ipsum quas illo<br>dolores ut voluptatem explicabo</p>
  </div>
  <div class="abs" style="left:896px;top:1320px;width:34px;height:34px;border-radius:50%;background:rgba(255,255,255,.85)"></div>
  <svg class="abs" style="left:904px;top:1328px" width="18" height="18" viewBox="0 0 18 18"><circle cx="7.5" cy="7.5" r="5" fill="none" stroke="#444" stroke-width="2"/><path d="M11 11l5 5" stroke="#444" stroke-width="2"/></svg>

  <!-- services -->
  <div class="abs rule" style="top:1519px"></div>
  <div class="abs service-title"><span>Our service</span></div>

  <div class="abs service" style="left:183px;top:1561px"><span class="num">1</span><div><h4>Ipsa explicabo</h4><p>Dolores ut voluptatem doloremque beatae ratione dolores unde</p></div></div>
  <div class="abs service" style="left:398px;top:1561px"><span class="num">3</span><div><h4>Ratione inventore</h4><p>Dolores ut voluptatem doloremque beatae ratione dolores unde</p></div></div>
  <div class="abs service" style="left:612px;top:1561px"><span class="num">5</span><div><h4>Unde quasi</h4><p>Dolores ut voluptatem doloremque beatae ratione dolores unde</p></div></div>
  <div class="abs service" style="left:827px;top:1561px"><span class="num">7</span><div><h4>Atione ratione</h4><p>Dolores ut voluptatem doloremque beatae ratione dolores unde</p></div></div>
  <div class="abs service" style="left:183px;top:1639px"><span class="num">2</span><div><h4>Ratione dolores</h4><p>Dolores ut voluptatem doloremque beatae ratione dolores unde</p></div></div>
  <div class="abs service" style="left:398px;top:1639px"><span class="num">4</span><div><h4>Beatae quia</h4><p>Dolores ut voluptatem doloremque beatae ratione dolores unde</p></div></div>
  <div class="abs service" style="left:612px;top:1639px"><span class="num">6</span><div><h4>Beatae atione</h4><p>Dolores ut voluptatem doloremque beatae ratione dolores unde</p></div></div>
  <div class="abs service" style="left:827px;top:1639px"><span class="num">8</span><div><h4>Ratione dolores</h4><p>Dolores ut voluptatem doloremque beatae ratione dolores unde</p></div></div>

  <div class="abs rule" style="top:1737px"></div>

  <!-- upcoming events -->
  <div class="abs col-head" style="left:181px;top:1792px">Upcoming events</div>
  <div class="abs more" style="left:358px;top:1793px;color:#999">view more <i style="background:#8f8f8f"><svg width="8" height="8" viewBox="0 0 8 8"><path d="M2 1l4 3-4 3" stroke="#fff" stroke-width="1.6" fill="none"/></svg></i></div>
  <div class="abs event" style="top:1830px">
    <div class="date">10<small>Jan</small></div>
    <div><h5>Veritatis beatae eos aut voluptas</h5><div class="meta">Doloremque, Totam / 5 Comments</div>
    <p>Enim accusantium laudantium perspiciatis ipsam sed doloremque ipsam totam unde unde, et aut illo aut</p></div>
  </div>
  <div class="abs event" style="top:1936px">
    <div class="date past">10<small>Jan</small></div>
    <div><h5 class="dark">Perspiciatis error natus aut eaque</h5><div class="meta">Doloremque, Totam / 5 Comments</div>
    <p>dolores totam unde unde, et aut illo aut veritatis explicabo dicta ipsa veniets</p></div>
  </div>

  <!-- popular news -->
  <div class="abs col-head" style="left:488px;top:1792px">Popular news</div>
  <div class="abs news" style="top:1823px"><span class="box open">−</span><span>Doloremque perspiciatis error</span></div>
  <p class="abs" style="left:488px;top:1862px;width:250px;font-size:10px;line-height:14px">Enim accusantium laudantium perspiciatis ipsam sed doloremque ipsam totam unde unde, et aut illo aut</p>
  <div class="abs news hot" style="top:1928px"><span class="box">+</span><span>Fugit aut illo omnis explicabo ipsa</span></div>
  <div class="abs news" style="top:1966px"><span class="box">+</span><span>Rem ipsum quas illo dolores</span></div>
  <div class="abs news" style="top:2003px"><span class="box">+</span><span>Voluptatem doloremque perspiciatis</span></div>

  <!-- testimonial -->
  <div class="abs col-head" style="left:762px;top:1792px">What they says</div>
  <div class="abs quote">
    <span class="quote-mark" style="left:16px;top:8px">“</span>
    Voluptatem Fugit aut illo omnis explicabo ipsa nemo enim ipsam ex voluptatem doloremque perspiciatis beatae magni architecto odit
    <span class="quote-mark" style="right:10px;bottom:6px">”</span>
  </div>
  <div class="abs" style="left:880px;top:1940px;text-align:right;width:84px">
    <div style="color:var(--red);font-size:11px;font-weight:700">Ben Carver</div>
    <div style="font-size:10px;color:#444">Project Manager</div>
  </div>
  <div class="abs" style="left:975px;top:1936px;width:40px;height:40px;background:linear-gradient(180deg,#c9cfd6,#6d7a8a)" role="img" aria-label="Portrait photo of the client"></div>

  <!-- slogan band -->
  <div class="abs band"></div>
  <div class="abs slogan-img" role="img" aria-label="Photo of a welder at work with sparks beside a yellow steel structure"></div>
  <div class="abs slogan-tag">Your slogan</div>
  <div class="abs top-project">
    <h3>Our top project of year</h3>
    <p>Lorem ipsum dolor sit amet voluptatem fugit aut illo omnis explicabo ipsa nemo enim ipsam ex doloremque labore et voluptatem doloremque</p>
    <div class="more">view more <i><svg width="8" height="8" viewBox="0 0 8 8"><path d="M2 1l4 3-4 3" stroke="#c4000b" stroke-width="1.6" fill="none"/></svg></i></div>
  </div>

  <!-- footer -->
  <div class="abs footer"></div>
  <div class="abs footer-col" style="left:141px;top:2377px;width:200px">
    <h4>About us</h4>
    <p>Fugit aut illo omnis explicabo ipsa ipsa, nemo enim ipsam quasi dolores voluptatem doloremque perspiciatis beatae magni architecto odit odit</p>
    <div class="footer-link" style="margin-top:22px">Read More <svg width="12" height="12" viewBox="0 0 12 12"><circle cx="6" cy="6" r="6" fill="#cfcfcf"/><path d="M5 3.5l2.5 2.5L5 8.5" stroke="#2b2b2b" stroke-width="1.4" fill="none"/></svg></div>
  </div>
  <div class="abs footer-col" style="left:398px;top:2377px;width:200px">
    <h4>Adreess</h4>
    <p>PO BOX 2210<br>Harbor Lane West, Bay City 3201<br>Coastland<br>+61 300 555 019</p>
    <div class="footer-link" style="margin-top:22px"><svg width="10" height="14" viewBox="0 0 10 14"><path d="M5 0a5 5 0 0 1 5 5c0 4-5 9-5 9S0 9 0 5a5 5 0 0 1 5-5z" fill="#cfcfcf"/><circle cx="5" cy="5" r="2" fill="#2b2b2b"/></svg> Open City Maps</div>
  </div>
  <div class="abs footer-col" style="left:614px;top:2377px">
    <h4>From Snapline</h4>
  </div>
  <div class="abs thumb" style="left:614px;top:2415px" role="img" aria-label="Thumbnail of a tower climber against blue sky"></div>
  <div class="abs thumb" style="left:702px;top:2415px;background:linear-gradient(180deg,#5a8fd0,#b8cbe0)" role="img" aria-label="Thumbnail of antennas on a monopole"></div>
  <div class="abs thumb" style="left:614px;top:2469px;background:linear-gradient(180deg,#4e84c8,#a7c0de)" role="img" aria-label="Thumbnail of antenna mounts"></div>
  <div class="abs thumb" style="left:702px;top:2469px;background:linear-gradient(180deg,#6c96c8,#c7d3df)" role="img" aria-label="Thumbnail of a lattice tower"></div>
  <div class="abs footer-col" style="left:844px;top:2377px;width:230px">
    <h4>Stay update with us!</h4>
    <p style="margin-top:10px">Tation patrioque ius id, rationibus pomeri adversarium ea congue sententiae</p>
  </div>
  <div class="abs subscribe"><span class="field">enter your email</span><span class="send">subscribe</span></div>

  <div class="abs bottombar"></div>
  <div class="abs copyright">© 2014 Your Company</div>
  <div class="abs legal">
    <span>about us</span><span class="sep">|</span><span>privacy policy</span><span class="sep">|</span><span>career</span><span class="sep">|</span><span>FAQs</span><span class="sep">|</span><span>contact us</span>
  </div>
  <div class="abs social"><span></span><span></span><span></span><span></span><span></span></div>

</div>
</body>
</html>
```